Business Card That Looks Like a Sports Card

Want it to look like a sports trading card. That front should have a baseball player. The back will list our contact info and website info etc.

Contact Information for Business Card

www.ridgecrestathletics.example
visitRCX.example
Email: marcus@ridgecrestathletics.example

Colors

Designer to choose colors to be used in the design.

Requirements
Must have
• Use our current logo and color scheme. Must look like a sports trading card.

```html
<!DOCTYPE html>
<html lang="en">
<head>
<meta charset="utf-8">
<title>Ridgecrest Athletics – Trading Card Business Card</title>
<link href="https://fonts.googleapis.com/css2?family=Montserrat:wght@400;600;800&display=swap" rel="stylesheet">
<style>
  :root {
    --stage: #eef0f2;
    --card-dark-1: #33363a;
    --card-dark-2: #0c0d0f;
    --card-light: #dcdfe3;
    --accent: #3aa88a;
    --ink: #3a3d42;
    --white: #ffffff;
    --photo-1: #2c4f8f;
    --photo-2: #6b4a2e;
    --photo-3: #1a1c22;
  }
  html, body {
    margin: 0;
    width: 1200px;
    height: 855px;
    overflow: hidden;
    background: var(--stage);
    font-family: "Montserrat", sans-serif;
  }
  .stage {
    position: relative;
    width: 1200px;
    height: 855px;
    display: flex;
    align-items: center;
    justify-content: center;
    gap: 40px;
  }
  .card {
    width: 540px;
    height: 310px;
    border-radius: 8px;
    overflow: hidden;
    box-shadow: 0 14px 30px rgba(0,0,0,0.25);
  }
  .card svg { display: block; }
  .brand-name { font-family: "Montserrat", sans-serif; font-weight: 800; letter-spacing: 1px; }
  .company-title { font-family: "Montserrat", sans-serif; font-weight: 400; font-size: 20px; fill: var(--ink); }
  .contact-line { font-family: "Montserrat", sans-serif; font-weight: 400; font-size: 13px; fill: var(--ink); }
</style>
</head>
<body>
<main class="stage">

  <section class="card card-front" aria-label="Card front">
    <svg width="540" height="310" viewBox="0 0 540 310">
      <defs>
        <linearGradient id="front-bg" x1="0" y1="0" x2="1" y2="1">
          <stop offset="0" stop-color="var(--card-dark-1)"/>
          <stop offset="1" stop-color="var(--card-dark-2)"/>
        </linearGradient>
        <linearGradient id="player-photo" x1="0" y1="1" x2="1" y2="0">
          <stop offset="0" stop-color="var(--photo-3)"/>
          <stop offset="0.45" stop-color="var(--photo-2)"/>
          <stop offset="1" stop-color="var(--photo-1)"/>
        </linearGradient>
      </defs>
      <rect width="540" height="310" fill="url(#front-bg)"/>
      <polygon points="220,0 540,0 540,310 400,310" fill="url(#player-photo)"
               role="img" aria-label="Photo of a baseball player holding out a glove with a ball"/>
      <g class="accent-stripes" stroke="var(--accent)" stroke-width="6">
        <line x1="200" y1="20" x2="420" y2="270"/>
        <line x1="275" y1="130" x2="375" y2="240"/>
        <line x1="345" y1="0" x2="440" y2="100"/>
        <line x1="420" y1="40" x2="470" y2="95"/>
      </g>
      <g class="front-brand">
        <circle cx="110" cy="215" r="14" fill="var(--accent)"/>
        <text class="brand-name" x="132" y="212" font-size="20" fill="var(--white)">RIDGECREST</text>
        <text class="brand-name" x="132" y="234" font-size="20" fill="var(--white)">ATHLETICS</text>
      </g>
    </svg>
  </section>

  <section class="card card-back" aria-label="Card back">
    <svg width="540" height="310" viewBox="0 0 540 310">
      <defs>
        <linearGradient id="glove-photo" x1="0" y1="0" x2="1" y2="1">
          <stop offset="0" stop-color="var(--photo-3)"/>
          <stop offset="0.5" stop-color="var(--photo-2)"/>
          <stop offset="1" stop-color="var(--photo-3)"/>
        </linearGradient>
      </defs>
      <rect width="540" height="310" fill="var(--card-light)"/>
      <polygon points="340,0 540,0 540,310 300,310" fill="url(#glove-photo)"
               role="img" aria-label="Close-up photo of a baseball glove holding a ball"/>
      <g class="accent-stripes" stroke="var(--accent)" stroke-width="4">
        <line x1="318" y1="20" x2="318" y2="120"/>
        <line x1="332" y1="10" x2="332" y2="215"/>
        <line x1="306" y1="130" x2="306" y2="295"/>
        <line x1="500" y1="170" x2="500" y2="270"/>
        <line x1="520" y1="160" x2="520" y2="190"/>
      </g>
      <g class="back-brand">
        <rect x="28" y="48" width="14" height="14" fill="var(--accent)"/>
        <text class="brand-name" x="48" y="60" font-size="11" fill="var(--ink)">RIDGECREST ATHLETICS</text>
      </g>
      <text class="company-title" x="28" y="115">RIDGECREST ATHLETICS</text>
      <g class="contact-list">
        <text class="contact-line" x="28" y="180" text-decoration="underline">marcus@ridgecrestathletics.example</text>
        <text class="contact-line" x="28" y="200" text-decoration="underline">www.ridgecrestathletics.example</text>
        <text class="contact-line" x="28" y="220">visitRCX.example</text>
        <text class="contact-line" x="28" y="240">880 Lantern Ridge Way, Suite 300,</text>
        <text class="contact-line" x="28" y="260">Brookfield, Indiana 46100</text>
      </g>
    </svg>
  </section>

</main>
</body>
</html>
```